Corporate Template

Looking for a set of corporate slides to be made which contain multiple different slides and orientations. Looking for at least 8 to 10 different master pages plus a Coversheet and closeout page. Incorporating a color palate similar to our logo coloring is preferred.

I have attached a logo.

```html
<!DOCTYPE html>
<html lang="en">
<head>
<meta charset="utf-8">
<title>Norbridge Partners – Corporate Slide Template</title>
<link href="https://fonts.googleapis.com/css2?family=Open+Sans:ital,wght@0,300;0,400;0,600;0,700;1,400;1,600&display=swap" rel="stylesheet">
<style>
:root{
  --blue:#1a73c9;
  --blue-light:#4c93d6;
  --cyan:#16a4e0;
  --grey:#8c8c8c;
  --text:#555;
  --text-soft:#a5a5a5;
  --canvas:#e3e4e6;
  --white:#fff;
}
*{box-sizing:border-box;margin:0;padding:0}
html,body{width:1200px;height:900px;overflow:hidden;background:var(--canvas);font-family:"Open Sans",Arial,sans-serif;color:var(--text)}
.board{position:relative;width:1200px;height:900px}
.slide{position:absolute;width:357px;height:276px;background:var(--white);overflow:hidden}
.slide--blue{background:var(--blue)}
.col-1{left:46px}.col-2{left:416px}.col-3{left:790px}
.row-1{top:26px}.row-2{top:314px}.row-3{top:604px}
.abs{position:absolute}
.band-bottom{position:absolute;left:0;right:0;bottom:0;height:6px;background:var(--blue)}
.page-num{position:absolute;right:4px;bottom:0;font-size:3px;color:var(--white)}
.slide-title{position:absolute;left:11px;top:11px;width:335px;font-weight:300;font-size:13px;color:var(--blue);border-bottom:1px solid #c9c9c9;line-height:1.1;padding-bottom:1px}
.brand{display:flex;align-items:center;gap:3px;font-weight:400;color:var(--blue);white-space:nowrap}
.brand-dot{border-radius:50%;background:var(--grey)}
.brand--footer{position:absolute;left:8px;bottom:13px;font-size:6px}
.brand--footer .brand-dot{width:4px;height:4px}
.brand--white{color:var(--white)}
.brand--white .brand-dot{background:var(--white)}
.photo{position:absolute;background:linear-gradient(135deg,#c8c8c8,#7d7d7d)}
.body-copy{font-size:5.3px;line-height:1.75;text-align:justify;color:var(--text)}
.body-copy p+p{margin-top:7px}
.cover-panel{position:absolute;left:5px;top:5px;width:348px;height:161px;background:var(--blue)}
.cover-rule{position:absolute;left:5px;top:167px;width:348px;height:2px;background:var(--blue-light)}
.cover-heading{position:absolute;right:22px;top:80px;text-align:right;color:var(--white);font-weight:300;font-size:15px;line-height:1.25}
.cover-sub{position:absolute;right:22px;top:125px;color:var(--white);font-size:7.5px;font-weight:300}
.brand--cover{position:absolute;right:22px;top:229px;font-size:15px}
.brand--cover .brand-dot{width:9px;height:9px;margin-right:2px}
.lead-caps{font-size:5.3px;line-height:1.75;color:var(--blue);text-transform:uppercase}
.quote-band{position:absolute;left:0;right:0;top:61px;height:62px;background:var(--blue)}
.quote-band p{position:absolute;left:148px;right:26px;top:13px;color:var(--white);font-style:italic;font-weight:600;font-size:5.5px;line-height:2.3;text-align:justify}
.chart{position:absolute;left:0;top:0}
.legend{position:absolute;top:210px;width:80px}
.legend h4{font-size:5px;font-weight:400;color:var(--text);display:flex;align-items:center;gap:3px}
.legend h4 i{display:inline-block;width:5px;height:5px}
.legend p{font-size:3.4px;line-height:1.5;margin-left:9px;color:var(--text);text-align:justify}
.service{position:absolute;top:79px;width:96px;text-align:center}
.service-icon{display:block;margin:0 auto;width:43px;height:43px}
.service h3{margin-top:15px;font-size:8px;font-weight:700;color:var(--blue)}
.service p{margin-top:3px;font-size:4.9px;line-height:1.45;color:var(--text-soft)}
.team-intro{position:absolute;left:20px;right:20px;top:53px;text-align:center;font-style:italic;font-weight:600;font-size:5px;line-height:2.1;color:var(--text)}
.member{position:absolute;top:88px;width:72px;text-align:center}
.member .portrait{display:block;width:52px;height:52px;margin:0 auto;border-radius:50%;border:1.5px solid var(--blue);background:linear-gradient(135deg,#d5d5d5,#858585)}
.member h3{margin-top:8px;font-size:6px;font-weight:400;color:var(--blue)}
.member h4{font-size:4.5px;font-style:italic;font-weight:400;color:var(--text)}
.member p{margin-top:9px;font-size:4.8px;line-height:2;text-align:justify;color:var(--text-soft)}
.image-title{position:absolute;left:13px;top:14px;color:var(--white);font-weight:300;font-size:13px}
.image-copy{position:absolute;left:22px;top:96px;width:148px;color:var(--white)}
.image-copy h3{font-size:5.3px;font-weight:400;margin-bottom:7px}
.image-copy p{font-size:4.6px;line-height:1.75;text-align:justify}
.image-copy p+p{margin-top:7px}
.section-mark{position:absolute;left:177px;top:108px}
.section-rule{position:absolute;left:128px;top:163px;width:102px;height:1px;background:rgba(255,255,255,.7)}
.section-title{position:absolute;left:0;right:0;top:170px;text-align:center;color:var(--white);font-weight:300;font-size:11.5px}
.close-panel{position:absolute;left:0;right:0;top:102px;bottom:0;background:var(--blue)}
.brand--close{position:absolute;left:21px;top:59px;font-size:15px}
.brand--close .brand-dot{width:9px;height:9px;margin-right:2px}
.thanks{position:absolute;right:25px;top:121px;text-align:right;color:var(--white)}
.thanks h2{font-weight:300;font-size:12px}
.thanks p{font-size:5px}
.contact{position:absolute;right:25px;top:203px;list-style:none;color:var(--white);font-size:5px;text-align:right}
.contact li{display:flex;align-items:center;justify-content:flex-end;gap:4px;margin-bottom:9px;line-height:1.3}
.contact svg{flex:none}
</style>
</head>
<body>
<main class="board">

  <section class="slide col-1 row-1">
    <div class="cover-panel"></div>
    <div class="cover-rule"></div>
    <h1 class="cover-heading">WELCOME<br>TO OUR PRESENTATION</h1>
    <p class="cover-sub">Birmingham, March 25, 2011</p>
    <div class="brand brand--cover"><span class="brand-dot"></span>Norbridge Partners</div>
    <div class="band-bottom"></div>
  </section>

  <section class="slide col-2 row-1">
    <h2 class="slide-title">ABOUT US</h2>
    <div class="photo" style="left:11px;top:35px;width:332px;height:78px" role="img" aria-label="Black and white photo of a business team gathered around a table"></div>
    <p class="lead-caps abs" style="left:11px;top:129px;width:102px">Lorem ipsum dolor sit met consectur adipsicing elit, sed do euismod tempor incididiunt ut labore et delore magna</p>
    <div class="body-copy abs" style="left:131px;top:128px;width:205px">
      <p>Lorem ipsum dolor sit amet, consectetur adipisicing elit, sed do eiusmod tempor incididunt ut labore et dolore magna aliqua. Ut enim ad minim veniam, quis nostrud exercitation ullamco laboris nisi ut aliquip ex ea commodo consequat. Duis aute irure dolor in reprehenderit in voluptate velit esse cillum dolore eu fugiat nulla pariatur.</p>
      <p>Lorem ipsum dolor sit amet, consectetur adipisicing elit, sed do eiusmod tempor incididunt ut labore et dolore magna aliqua. Ut enim ad minim veniam, quis nostrud exercitation ullamco laboris nisi ut aliquip ex ea commodo consequat. Duis aute irure dolor in reprehenderit in voluptate velit esse cillum dolore eu</p>
    </div>
    <div class="brand brand--footer"><span class="brand-dot"></span>Norbridge Partners</div>
    <div class="band-bottom"><span class="page-num">1</span></div>
  </section>

  <section class="slide col-3 row-1">
    <h2 class="slide-title">ABOUT US</h2>
    <div class="quote-band"><p>Lorem ipsum dolor sit amet<br>consectetur adipisicing elit, sed do eiusmod tempor incididunt ut labore et dolore magna aliqua. Ut enim ad</p></div>
    <div class="photo" style="left:16px;top:46px;width:106px;height:83px" role="img" aria-label="Black and white portrait of a smiling businesswoman"></div>
    <div class="body-copy abs" style="left:148px;top:132px;width:182px;font-size:4.6px">
      <p>Lorem ipsum dolor sit amet, consectetur adipisicing elit, sed do eiusmod tempor incididunt ut labore et dolore magna aliqua. Ut enim ad minim veniam, quis nostrud exercitation ullamco laboris nisi ut aliquip ex ea commodo consequat. Duis aute irure dolor in reprehenderit in voluptate velit esse cillum dolore eu fugiat nulla pariatur.</p>
      <p>Lorem ipsum dolor sit amet, consectetur adipisicing elit, sed do eiusmod tempor incididunt ut labore et dolore magna aliqua. Ut enim ad minim veniam, quis nostrud exercitation ullamco laboris nisi ut aliquip ex ea commodo consequat. Duis aute irure dolor in reprehenderit in voluptate velit esse cillum dolore eu</p>
      <p>fugiat nulla pariatur. Excepteur sint occaecat cupidatat non proident, sunt in culpa qui officia deserunt mollit anim id est laborum. Excepteur sint occaecat cupidatat non proident, sunt in consequat. Duis aute irure dolor in reprehenderit</p>
    </div>
    <div class="brand brand--footer"><span class="brand-dot"></span>Norbridge Partners</div>
    <div class="band-bottom"><span class="page-num">1</span></div>
  </section>

  <section class="slide col-1 row-2">
    <h2 class="slide-title">ABOUT US</h2>
    <svg class="chart" width="357" height="276" viewBox="0 0 446 345" aria-label="Bar chart of three series from 2009 to 2012">
      <g stroke="#777" stroke-width="1">
        <line x1="88" y1="64" x2="88" y2="219"/>
        <line x1="88" y1="219" x2="356" y2="219"/>
        <line x1="84" y1="64" x2="88" y2="64"/><line x1="84" y1="90" x2="88" y2="90"/>
        <line x1="84" y1="116" x2="88" y2="116"/><line x1="84" y1="142" x2="88" y2="142"/>
        <line x1="84" y1="168" x2="88" y2="168"/><line x1="84" y1="194" x2="88" y2="194"/>
      </g>
      <g fill="#1a73c9">
        <rect x="98" y="107" width="16" height="112"/><rect x="164" y="138" width="16" height="81"/>
        <rect x="231" y="118" width="16" height="101"/><rect x="298" y="122" width="16" height="97"/>
      </g>
      <g fill="#8c8c8c">
        <rect x="114" y="157" width="16" height="62"/><rect x="180" y="107" width="16" height="112"/>
        <rect x="247" y="170" width="16" height="49"/><rect x="314" y="159" width="16" height="60"/>
      </g>
      <g fill="#16a4e0">
        <rect x="130" y="168" width="15" height="51"/><rect x="196" y="168" width="15" height="51"/>
        <rect x="263" y="148" width="15" height="71"/><rect x="330" y="111" width="15" height="108"/>
      </g>
      <g fill="#1a73c9" font-family="Open Sans, Arial, sans-serif" font-size="12" text-anchor="middle">
        <text x="122" y="243">2009</text><text x="189" y="243">2010</text>
        <text x="255" y="243">2011</text><text x="322" y="243">2012</text>
      </g>
    </svg>
    <div class="legend" style="left:60px"><h4><i style="background:var(--blue)"></i>LOREM IPSUM</h4><p>Lorem ipsum dolor sit amet, consectetur adipisicing elit, sed do eiusmod tempor incididunt ut labore et dolore magna</p></div>
    <div class="legend" style="left:159px"><h4><i style="background:var(--grey)"></i>LOREM IPSUM</h4><p>Lorem ipsum dolor sit amet, consectetur adipisicing elit, sed do eiusmod tempor incididunt ut labore et dolore magna</p></div>
    <div class="legend" style="left:255px"><h4><i style="background:var(--cyan)"></i>LOREM IPSUM</h4><p>Lorem ipsum dolor sit amet, consectetur adipisicing elit, sed do eiusmod tempor incididunt ut labore et dolore magna</p></div>
    <div class="brand brand--footer"><span class="brand-dot"></span>Norbridge Partners</div>
    <div class="band-bottom"><span class="page-num">1</span></div>
  </section>

  <section class="slide col-2 row-2">
    <h2 class="slide-title">ABOUT US</h2>
    <div class="service" style="left:19px">
      <svg class="service-icon" viewBox="0 0 44 44" aria-hidden="true">
        <circle cx="22" cy="22" r="22" fill="#1a73c9"/>
        <g fill="#fff"><circle cx="22" cy="22" r="8"/>
          <rect x="20" y="10" width="4" height="24"/><rect x="10" y="20" width="24" height="4"/>
          <rect x="20" y="10" width="4" height="24" transform="rotate(45 22 22)"/>
          <rect x="20" y="10" width="4" height="24" transform="rotate(-45 22 22)"/></g>
        <circle cx="22" cy="22" r="3.5" fill="#1a73c9"/>
      </svg>
      <h3>OUR SERVICES</h3>
      <p>dolor sit amet, consectetur adipisicing elit, sed do eiusmod tempor incididunt ut labore et dolore magna aliqua. Ut enim ad minim veniam, quis nostrud exercitation ullamco laboris nisi ut aliquip ex ea cesse cillum dolore eu fugiat nulla pariatur.</p>
    </div>
    <div class="service" style="left:131px">
      <svg class="service-icon" viewBox="0 0 44 44" aria-hidden="true">
        <circle cx="22" cy="22" r="22" fill="#8c8c8c"/>
        <g fill="#fff"><rect x="13" y="24" width="4" height="8"/><rect x="19" y="20" width="4" height="12"/><rect x="25" y="16" width="4" height="16"/>
          <path d="M12 21 L22 13 L27 15 L31 11 L32 14 L28 18 L22 16 L13 23 Z"/></g>
      </svg>
      <h3>OUR SERVICES</h3>
      <p>dolor sit amet, consectetur adipisicing elit, sed do eiusmod tempor incididunt ut labore et dolore magna aliqua. Ut enim ad minim veniam, quis nostrud exercitation ullamco laboris nisi ut aliquip ex ea cesse cillum dolore eu fugiat nulla pariatur.</p>
    </div>
    <div class="service" style="left:240px">
      <svg class="service-icon" viewBox="0 0 44 44" aria-hidden="true">
        <circle cx="22" cy="22" r="22" fill="#1a73c9"/>
        <g fill="none" stroke="#fff" stroke-width="2"><rect x="12" y="13" width="20" height="13"/>
          <line x1="10" y1="12" x2="34" y2="12"/><line x1="22" y1="26" x2="22" y2="30"/>
          <line x1="22" y1="28" x2="17" y2="33"/><line x1="22" y1="28" x2="27" y2="33"/></g>
      </svg>
      <h3>OUR SERVICES</h3>
      <p>dolor sit amet, consectetur adipisicing elit, sed do eiusmod tempor incididunt ut labore et dolore magna aliqua. Ut enim ad minim veniam, quis nostrud exercitation ullamco laboris nisi ut aliquip ex ea cesse cillum dolore eu fugiat nulla pariatur.</p>
    </div>
    <div class="brand brand--footer"><span class="brand-dot"></span>Norbridge Partners</div>
    <div class="band-bottom"><span class="page-num">1</span></div>
  </section>

  <section class="slide col-3 row-2">
    <h2 class="slide-title">ABOUT US</h2>
    <p class="team-intro">dolor sit amet, consectetur adipisicing elit, sed do eiusmod tempor incididunt ut labore et dolore magna aliqua.<br>Ut enim ad minim veniam, quis nostrud exercitation ullamco laboris nisi ut a</p>
    <div class="member" style="left:37px">
      <span class="portrait" role="img" aria-label="Portrait of the company president"></span>
      <h3>DANIEL REYES</h3><h4>President</h4>
      <p>dolor sit amet, consectetur adipisicing elit, sed do eiusmod tempor incididunt ut labore et dolore magna aliqua. Ut enim ad minim veniam, quis nostrud exercitation</p>
    </div>
    <div class="member" style="left:140px">
      <span class="portrait" role="img" aria-label="Portrait of the CEO and founder"></span>
      <h3>GRACE LINDQVIST</h3><h4>CEO / Founder</h4>
      <p>dolor sit amet, consectetur adipisicing elit, sed do eiusmod tempor incididunt ut labore et dolore magna aliqua. Ut enim ad minim veniam, quis nostrud exercitation</p>
    </div>
    <div class="member" style="left:240px">
      <span class="portrait" role="img" aria-label="Portrait of the vice president"></span>
      <h3>OLIVIA HART</h3><h4>Vice President</h4>
      <p>dolor sit amet, consectetur adipisicing elit, sed do eiusmod tempor incididunt ut labore et dolore magna aliqua. Ut enim ad minim veniam, quis nostrud exercitation</p>
    </div>
    <div class="brand brand--footer"><span class="brand-dot"></span>Norbridge Partners</div>
    <div class="band-bottom"><span class="page-num">1</span></div>
  </section>

  <section class="slide slide--blue col-1 row-3">
    <h2 class="image-title">IMAGE TEXT</h2>
    <div class="image-copy">
      <h3>LOREM IPSUM DOLOR SIT MET</h3>
      <p>Lorem ipsum dolor sit amet, consectetur adipisicing elit, sed do eiusmod tempor incididunt ut labore et dolore magna aliqua. Ut enim ad minim veniam, quis nostrud exercitation ullamco laboris nisi ut aliquip ex ea commodo consequat. Duis aute irure dolor in reprehenderit in voluptate velit esse cillum dolore eu fugiat nulla pariatur.</p>
      <p>Lorem ipsum dolor sit amet, consectetur adipisicing elit, sed do eiusmod tempor incididunt ut labore et dolore magna aliqua. Ut enim ad minim veniam, quis nostrud exercitation ullamco laboris nisi ut aliquip ex ea commodo consequat. Duis aute irure dolor in reprehenderit in voluptate velit esse cillum dolore eu</p>
    </div>
    <div class="photo" style="left:176px;top:0;width:181px;height:276px;background:linear-gradient(160deg,#efefef,#bdbdbd 55%,#5e5e5e)" role="img" aria-label="Black and white photo of two smiling young professionals"></div>
    <div class="brand brand--footer brand--white" style="bottom:9px"><span class="brand-dot"></span>Norbridge Partners</div>
  </section>

  <section class="slide slide--blue col-2 row-3">
    <svg class="section-mark" width="45" height="45" viewBox="0 0 45 45" aria-hidden="true">
      <circle cx="22.5" cy="22.5" r="22.5" fill="#fff"/>
      <circle cx="25" cy="12" r="3.6" fill="#1a73c9"/>
      <path d="M20 19 H27 L23 33 Q22.5 35 25 34 L26.5 33.3 L26 35.5 Q22 38 18.5 37 Q16 36 17 33 L20 23 H17.5 Z" fill="#1a73c9"/>
    </svg>
    <div class="section-rule"></div>
    <h2 class="section-title">SECTION TITLE</h2>
  </section>

  <section class="slide col-3 row-3">
    <div class="brand brand--close"><span class="brand-dot"></span>Norbridge Partners</div>
    <div class="close-panel"></div>
    <div class="thanks"><h2>THANK YOU</h2><p>FOR YOUR TIME</p></div>
    <ul class="contact">
      <li><span>4120 Cedar Ridge Road Ste 300<br>Millbrook, Ohio 44120</span>
        <svg width="8" height="8" viewBox="0 0 8 8"><circle cx="4" cy="4" r="4" fill="#fff"/><path d="M4 1.8 L6.2 4 H5.5 V6 H2.5 V4 H1.8 Z" fill="#1a73c9"/></svg></li>
      <li><span>1.800.555.0142</span>
        <svg width="8" height="8" viewBox="0 0 8 8"><circle cx="4" cy="4" r="4" fill="#fff"/><rect x="2" y="3" width="4" height="2.5" rx=".5" fill="#1a73c9"/></svg></li>
      <li><span>hello@norbridgepartners.com</span>
        <svg width="8" height="8" viewBox="0 0 8 8"><circle cx="4" cy="4" r="4" fill="#fff"/><rect x="2" y="2.6" width="4" height="2.8" fill="#1a73c9"/></svg></li>
      <li><span>www.norbridgepartners.com</span>
        <svg width="8" height="8" viewBox="0 0 8 8"><circle cx="4" cy="4" r="4" fill="#fff"/><circle cx="4" cy="4" r="2" fill="none" stroke="#1a73c9" stroke-width=".8"/></svg></li>
    </ul>
  </section>

</main>
</body>
</html>
```